Birthday Party Invitation for Jasper's 18th Birthday Party

Our eldest son Jasper is turning 18 and we are having a party at home to celebrate the occasion. This project is about creating an invitation that will go to our friends and family. We like things to be nicely designed so posting it to pixel harbor seemed to be the way to go.
The invitation needs to be able to be printed onto an A4 piece of paper. We have access to a color copier so it can be nice and bright.

We want an invitation that conveys a sense of occasion and looks as though we have put time and effort into having a great night to celebrate his 18th.
I have included some photo's of Jasper. They can go onto the invitation as is or they can be given some treatment to form a theme when on the invitiation. I'll leave the treatment of the photo's to the individual designer.

Target Market(s)

Friends and Family

Font styles to use
Sans Serif

Colors

Designer to choose colors to be used in the design.

Requirements
Must have
• The invitation must have the time, date and location of the party.
• Details:
• Saturday 29th of July 2017 7.00pm
• 41 Brackmere Lane, Fenwood
• Food and Drinks provided It must be bright and colourful and convey a sense of excitement.
Nice to have
• Inclusion of the photo's that I have uploaded.
Should not have
• any boring bits

```html
<!DOCTYPE html>
<html lang="en">
<head>
<meta charset="utf-8">
<title>Jasper is Turning 18 – Invitation</title>
<link rel="stylesheet" href="https://fonts.googleapis.com/css2?family=Josefin+Sans:wght@300;400;700&display=swap">
<style>
  :root {
    --night-deep: #1a1533;
    --night-violet: #3b2467;
    --night-plum: #4d2a6e;
    --ray: rgba(255, 255, 255, 0.07);
    --ink-white: #ffffff;
    --photo-disc: #24183f;
    --photo-pool: #4fb6d8;
    --photo-garden: #5f7f4a;
    --photo-blazer: #6a2030;
  }
  * { margin: 0; padding: 0; box-sizing: border-box; }
  html, body { width: 848px; height: 1200px; overflow: hidden; background: var(--night-deep); }
  .invitation {
    position: relative;
    width: 848px;
    height: 1200px;
    overflow: hidden;
    font-family: "Josefin Sans", sans-serif;
    color: var(--ink-white);
    background:
      radial-gradient(ellipse 60% 40% at 10% 10%, rgba(40, 110, 120, 0.55), transparent 70%),
      radial-gradient(ellipse 70% 45% at 85% 55%, rgba(120, 70, 170, 0.55), transparent 70%),
      radial-gradient(ellipse 80% 40% at 40% 75%, rgba(90, 50, 130, 0.5), transparent 70%),
      linear-gradient(180deg, #2c2a52 0%, var(--night-violet) 45%, var(--night-plum) 75%, #2a1a44 100%);
  }
  .backdrop, .gallery { position: absolute; inset: 0; }
  .headline {
    position: absolute;
    top: 818px;
    width: 100%;
    text-align: center;
    font-size: 63px;
    line-height: 1;
    text-transform: uppercase;
  }
  .headline .name, .headline .age { font-weight: 700; }
  .headline .verb { font-weight: 300; }
  .tagline {
    position: absolute;
    top: 912px;
    width: 100%;
    text-align: center;
    font-size: 39px;
    font-weight: 700;
    text-transform: uppercase;
    line-height: 1;
  }
  .subline {
    position: absolute;
    top: 968px;
    width: 100%;
    text-align: center;
    font-size: 24px;
    font-weight: 400;
    letter-spacing: 1.5px;
    text-transform: uppercase;
    line-height: 1;
  }
  .details {
    position: absolute;
    left: 98px;
    top: 1035px;
    width: 672px;
    height: 116px;
    border-top: 3px solid var(--ink-white);
    border-bottom: 3px solid var(--ink-white);
    text-align: center;
    font-size: 28px;
    font-weight: 700;
    text-transform: uppercase;
    line-height: 1;
  }
  .details .when { margin-top: 24px; }
  .details .where { margin-top: 16px; }
</style>
</head>
<body>
<main class="invitation">
  <svg class="backdrop" width="848" height="1200" viewBox="0 0 848 1200" aria-hidden="true">
    <g fill="var(--ray)">
      <polygon points="100,0 170,0 424,480"/>
      <polygon points="260,0 330,0 424,480"/>
      <polygon points="500,0 570,0 424,480"/>
      <polygon points="660,0 730,0 424,480"/>
      <polygon points="0,60 0,180 424,480"/>
      <polygon points="848,60 848,180 424,480"/>
    </g>
    <g fill="#ffffff" opacity="0.5">
      <circle cx="40" cy="140" r="1.5"/><circle cx="140" cy="260" r="1.2"/>
      <circle cx="780" cy="120" r="1.5"/><circle cx="810" cy="330" r="1.2"/>
      <circle cx="60" cy="820" r="1.4"/><circle cx="790" cy="760" r="1.3"/>
      <circle cx="120" cy="700" r="1.1"/><circle cx="720" cy="980" r="1.2"/>
      <circle cx="30" cy="1100" r="1.3"/><circle cx="820" cy="1130" r="1.2"/>
      <circle cx="200" cy="90" r="1"/><circle cx="640" cy="60" r="1"/>
    </g>
  </svg>

  <svg class="gallery" width="848" height="1200" viewBox="0 0 848 1200">
    <defs>
      <linearGradient id="portrait-fill" x1="0" y1="0" x2="0" y2="1">
        <stop offset="0" stop-color="#b99a86"/>
        <stop offset="0.45" stop-color="#6f6580"/>
        <stop offset="1" stop-color="#2c2946"/>
      </linearGradient>
      <linearGradient id="pool-fill" x1="0" y1="0" x2="0" y2="1">
        <stop offset="0" stop-color="#8fd3ea"/><stop offset="1" stop-color="var(--photo-pool)"/>
      </linearGradient>
      <linearGradient id="garden-fill" x1="0" y1="0" x2="0" y2="1">
        <stop offset="0" stop-color="var(--photo-garden)"/><stop offset="1" stop-color="#c9b4a6"/>
      </linearGradient>
      <linearGradient id="family-fill" x1="0" y1="0" x2="0" y2="1">
        <stop offset="0" stop-color="#5a4a3a"/><stop offset="1" stop-color="#3c4f7a"/>
      </linearGradient>
      <linearGradient id="blazer-fill" x1="0" y1="0" x2="0" y2="1">
        <stop offset="0" stop-color="#8db07a"/><stop offset="0.5" stop-color="#6f8fa0"/><stop offset="1" stop-color="var(--photo-blazer)"/>
      </linearGradient>
    </defs>

    <g class="feature-portrait">
      <circle cx="424" cy="478" r="242" fill="rgba(255,255,255,0.85)" stroke="#ffffff" stroke-width="2.5"/>
      <path role="img" aria-label="Portrait photo of Jasper smiling in a navy knit jumper"
            fill="url(#portrait-fill)"
            d="M216,90 Q216,20 290,20 L558,20 Q632,20 632,90 L632,620 L216,620 Z"/>
    </g>

    <g class="moment">
      <circle cx="142" cy="514" r="118" fill="var(--photo-disc)" stroke="#ffffff" stroke-width="2"/>
      <circle role="img" aria-label="Photo of Jasper playing water polo" cx="142" cy="514" r="108" fill="url(#pool-fill)"/>
    </g>
    <g class="moment">
      <circle cx="708" cy="516" r="114" fill="var(--photo-disc)" stroke="#ffffff" stroke-width="2"/>
      <circle role="img" aria-label="Photo of Jasper in his school blazer by the river" cx="708" cy="516" r="104" fill="url(#blazer-fill)"/>
    </g>
    <g class="moment">
      <circle cx="308" cy="664" r="118" fill="var(--photo-disc)" stroke="#ffffff" stroke-width="2"/>
      <circle role="img" aria-label="Photo of Jasper with his sister in the garden" cx="308" cy="664" r="108" fill="url(#garden-fill)"/>
    </g>
    <g class="moment">
      <circle cx="540" cy="658" r="118" fill="var(--photo-disc)" stroke="#ffffff" stroke-width="2"/>
      <circle role="img" aria-label="Photo of Jasper in a tuxedo with his parents" cx="540" cy="658" r="108" fill="url(#family-fill)"/>
    </g>
  </svg>

  <h1 class="headline"><span class="name">Jasper</span> <span class="verb">is turning</span> <span class="age">18</span></h1>
  <p class="tagline">Let’s celebrate his birthday</p>
  <p class="subline">and have lots of food and drinks!</p>
  <section class="details">
    <p class="when">Saturday | July 29, 2017 | 7.00pm</p>
    <p class="where">41 Brackmere Lane, Fenwood</p>
  </section>
</main>
</body>
</html>
```